Book Cover Design Project

I would like a book cover designed for a book entitled: Bright Days Ahead: Finding the Right Cosmetic Dentist
The target audience is those patients interested in cosmetic dentistry. Generally those would be people over 45, with above average income, but the cover should have more universal appeal.
The book was written by
Raymond T. Oakes, DDS, FSFDP
Fellow in the Society of Family Dental Practice
(that's me)
The book will be distributed as an ebook for free to patients and potential patients interested in cosmetic dentistry.

```html
<!DOCTYPE html>
<html lang="en">
<head>
<meta charset="utf-8">
<title>Bright Days Ahead – Book Cover</title>
<link rel="stylesheet" href="https://fonts.googleapis.com/css2?family=Fira+Sans:ital,wght@0,500;0,600;1,700;1,800&family=Mulish:wght@400;600&display=swap">
<style>
  :root {
    --stage: #e6e9eb;
    --paper: #ffffff;
    --sky: #5fd0ee;
    --sky-light: #a9e6f7;
    --ocean: #2d7aa8;
    --ocean-deep: #1f6690;
    --line-blue: #3a8ee8;
    --slate: #868c95;
    --slate-light: #a3a8ae;
    --photo-skin: #e7b9a0;
    --photo-shadow: #6a4335;
  }
  * { margin: 0; padding: 0; box-sizing: border-box; }
  html, body {
    width: 1200px;
    height: 900px;
    overflow: hidden;
    background: var(--stage);
  }
  .stage {
    width: 1200px;
    height: 900px;
    display: flex;
    align-items: center;
    justify-content: center;
  }
  .book-cover {
    position: relative;
    width: 656px;
    height: 846px;
    background: var(--paper);
    box-shadow: 0 6px 24px rgba(40, 55, 65, 0.25);
  }
  .cover-art {
    position: absolute;
    inset: 0;
    width: 656px;
    height: 846px;
  }
  .arc-subtitle {
    font-family: "Fira Sans", sans-serif;
    font-weight: 600;
    font-size: 31px;
    letter-spacing: 1px;
    fill: var(--ocean);
  }
  .book-title {
    font-family: "Fira Sans", sans-serif;
    font-style: italic;
    font-weight: 800;
    font-size: 66px;
    fill: var(--sky);
  }
  .author-block {
    position: absolute;
    left: 0;
    right: 0;
    top: 706px;
    text-align: center;
    font-family: "Mulish", sans-serif;
    color: var(--slate);
  }
  .author-name {
    font-weight: 600;
    font-size: 29px;
    letter-spacing: 0.5px;
    text-transform: uppercase;
    line-height: 36px;
  }
  .author-credentials {
    display: flex;
    align-items: center;
    justify-content: center;
    gap: 8px;
    margin: 4px auto 0;
    width: 380px;
    font-size: 11px;
    font-weight: 600;
    letter-spacing: 0.5px;
    color: var(--slate);
  }
  .author-credentials::before,
  .author-credentials::after {
    content: "";
    flex: 1;
    height: 1px;
    background: var(--slate-light);
  }
  .author-fellowship {
    margin-top: 4px;
    font-size: 16px;
    font-weight: 400;
    letter-spacing: 0.6px;
    color: var(--slate);
  }
</style>
</head>
<body>
<main class="stage">
  <article class="book-cover">
    <svg class="cover-art" viewBox="0 0 656 846" xmlns="http://www.w3.org/2000/svg">
      <defs>
        <linearGradient id="ring-outer" x1="0" y1="0" x2="1" y2="0.4">
          <stop offset="0" stop-color="var(--ocean-deep)"/>
          <stop offset="0.55" stop-color="var(--sky)"/>
          <stop offset="1" stop-color="var(--sky-light)" stop-opacity="0.3"/>
        </linearGradient>
        <linearGradient id="ring-inner" x1="0" y1="0" x2="1" y2="0">
          <stop offset="0" stop-color="var(--sky)"/>
          <stop offset="0.6" stop-color="var(--sky-light)"/>
          <stop offset="1" stop-color="var(--sky-light)" stop-opacity="0.2"/>
        </linearGradient>
        <linearGradient id="ring-lower" x1="0" y1="0" x2="1" y2="0">
          <stop offset="0" stop-color="var(--sky-light)" stop-opacity="0.4"/>
          <stop offset="0.4" stop-color="var(--ocean)"/>
          <stop offset="1" stop-color="var(--sky)"/>
        </linearGradient>
        <linearGradient id="photo-tone" x1="0" y1="0" x2="0" y2="1">
          <stop offset="0" stop-color="var(--photo-skin)"/>
          <stop offset="0.7" stop-color="#d69a82"/>
          <stop offset="1" stop-color="var(--photo-shadow)"/>
        </linearGradient>
        <linearGradient id="band-rule" x1="0" y1="0" x2="1" y2="0">
          <stop offset="0" stop-color="var(--line-blue)" stop-opacity="0"/>
          <stop offset="0.5" stop-color="var(--line-blue)"/>
          <stop offset="1" stop-color="var(--line-blue)" stop-opacity="0"/>
        </linearGradient>
        <filter id="soft-shadow" x="-20%" y="-20%" width="140%" height="140%">
          <feDropShadow dx="0" dy="4" stdDeviation="8" flood-color="#6a7c88" flood-opacity="0.25"/>
        </filter>
        <clipPath id="photo-clip">
          <rect x="0" y="0" width="656" height="406"/>
        </clipPath>
        <path id="subtitle-arc" d="M 104 393 A 228 228 0 1 1 560 393"/>
      </defs>

      <!-- emblem rings -->
      <circle cx="330" cy="375" r="300" fill="none" stroke="url(#ring-outer)" stroke-width="10"/>
      <circle cx="330" cy="375" r="284" fill="none" stroke="url(#ring-inner)" stroke-width="5"/>
      <path d="M 120 600 A 300 300 0 0 0 560 600" fill="none" stroke="url(#ring-lower)" stroke-width="10"/>

      <!-- inner white disc -->
      <circle cx="332" cy="373" r="262" fill="var(--paper)" filter="url(#soft-shadow)"/>

      <!-- photo area -->
      <g clip-path="url(#photo-clip)">
        <circle cx="332" cy="373" r="212" fill="var(--paper)" filter="url(#soft-shadow)"/>
        <circle cx="332" cy="373" r="200" fill="url(#photo-tone)" role="img" aria-label="Close-up photograph of a smiling mouth with bright white teeth"/>
      </g>

      <!-- arched subtitle -->
      <text class="arc-subtitle">
        <textPath href="#subtitle-arc" startOffset="50%" text-anchor="middle">FINDING THE RIGHT COSMETIC DENTIST</textPath>
      </text>

      <!-- title band -->
      <rect x="0" y="406" width="656" height="170" fill="var(--paper)" filter="url(#soft-shadow)"/>
      <rect x="40" y="414" width="576" height="3" fill="url(#band-rule)"/>
      <rect x="40" y="562" width="576" height="3" fill="url(#band-rule)"/>
      <text class="book-title" x="328" y="514" text-anchor="middle">Bright Days Ahead</text>
    </svg>

    <div class="author-block">
      <p class="author-name">Raymond T. Oakes</p>
      <p class="author-credentials">DDS, FSFDP</p>
      <p class="author-fellowship">Fellow in the Society of Family Dental Practice</p>
    </div>
  </article>
</main>
</body>
</html>
```